Newspaper AD in the Restaurant Section HOMECARE/Senior Living

Looking for an ad that is 6.425 inches wide and 5 inches tall to go into the newspaper weekly it will be in the restaurant section. We are a senior homecare company and we are looking to show clients that caregivers are able to assist them not only in personal care needs but also meal prep. We would like the design to have the feel of our existing ad or our newly launched website. It will be in the Savor section of the Pacific Morning Ledger which is not where we normally would advertise as a homecare agency so ad has to have some kind of feel for that section.
It should say somewhere maybe by contact info Call today for FREE Consultation.

Target Market(s)

Target market is Men/Women ages 35-105

Industry/Entity Type

Homecare and Senior Living

Font styles to use
Sans Serif

Colors
0054AA
0677BA
7BADD7
CADEEF
E8F1F8
FFF300
FFF600
FEFA6F
FFFEC7
FFFEE8
EB3D1F
EC4F4E
F09395
F8D3D4
FCEDEE

Requirements
Must have
• Logo, Contact info: Phone number (808) 555-0173, email address Info@brightmeadowcare.com and website www.Brightmeadowcare.com.
Nice to have
• Something that will be eye catching and to the point. Maybe a picture of a caregiver preparing a meal with an elderly person

```html
<!DOCTYPE html>
<html lang="en">
<head>
<meta charset="utf-8">
<title>Brightmeadow Homecare – Newspaper Ad</title>
<link rel="stylesheet" href="https://fonts.googleapis.com/css2?family=Open+Sans:wght@400;600;700;800&display=swap">
<style>
  :root{
    --blue-deep:#0054AA;
    --blue:#0677BA;
    --blue-soft:#7BADD7;
    --blue-pale:#CADEEF;
    --blue-mist:#E8F1F8;
    --coral:#EC4F4E;
    --coral-strong:#EB3D1F;
    --pink:#F09395;
    --pink-soft:#F8D3D4;
    --pink-mist:#FCEDEE;
    --white:#FFFFFF;
    --ink:#2B3A4A;
    --stage:#EDEDED;
  }
  *{box-sizing:border-box;margin:0;padding:0}
  html,body{width:682px;height:1200px;overflow:hidden;background:var(--stage);font-family:"Open Sans",sans-serif}
  .ad{position:absolute;left:0;top:335px;width:682px;height:530px;background:var(--white);overflow:hidden;box-shadow:0 4px 14px rgba(0,0,0,.12)}

  .photo-main{position:absolute;left:296px;top:0;width:386px;height:474px;background:linear-gradient(135deg,#8a5a3c 0%,#c79a72 45%,#e9d3b7 75%,#a8705a 100%)}
  .photo-curve{position:absolute;left:256px;top:0;width:110px;height:474px;z-index:1}
  .photo-inset{position:absolute;left:300px;top:240px;width:160px;height:160px;border-radius:50%;border:5px solid var(--white);background:radial-gradient(circle at 45% 40%,#c6a08a 0%,#5b7fa8 60%,#34587f 100%);box-shadow:0 2px 8px rgba(0,0,0,.2);z-index:2}

  .left-column{position:absolute;left:0;top:0;width:268px;height:474px;z-index:3}
  .brand{position:absolute;left:0;top:22px;width:268px;display:flex;flex-direction:column;align-items:center;gap:8px}
  .brand-mark{width:40px;height:40px;background:var(--coral);border-radius:6px}
  .brand-name{font-weight:700;font-size:21px;color:var(--blue-deep);line-height:1.1;text-align:center}
  .headline{position:absolute;left:22px;top:150px;width:246px;font-weight:800;font-size:16.5px;line-height:1.25;color:var(--blue-deep)}
  .services-tab{position:absolute;left:22px;top:256px;width:190px;height:30px;background:var(--coral);color:var(--white);font-weight:700;font-size:15px;line-height:30px;padding-left:12px;border-radius:0 15px 15px 0}
  .services{position:absolute;left:22px;top:296px;list-style:none}
  .services li{display:flex;align-items:center;gap:8px;font-size:13px;color:var(--ink);height:23px;white-space:nowrap}
  .services svg{width:14px;height:14px;flex:none}
  .consult{position:absolute;left:22px;top:420px;font-size:13px;font-weight:700;color:var(--coral);white-space:nowrap}
  .heart-accent{position:absolute;left:232px;top:442px;width:26px;height:22px}

  .contact-bar{position:absolute;left:0;bottom:0;width:682px;height:56px;background:var(--blue);display:flex;align-items:center;padding:0 18px;gap:18px;color:var(--white);z-index:3}
  .call-pill{display:flex;align-items:center;gap:8px;background:var(--coral);border-radius:20px;padding:7px 14px;font-weight:700;white-space:nowrap;flex:none}
  .call-label{font-size:14px}
  .call-number{font-size:16px}
  .contact-item{display:flex;align-items:center;gap:6px;font-size:12px;font-weight:600;white-space:nowrap}
  .contact-item svg,.call-pill svg{width:15px;height:15px;flex:none}
</style>
</head>
<body>
<main class="ad">
  <div class="photo-main" role="img" aria-label="Caregiver in red scrubs serving a meal to seniors at a dining table"></div>
  <svg class="photo-curve" viewBox="0 0 110 474" preserveAspectRatio="none" aria-hidden="true">
    <path d="M0 0H40C20 150 30 330 80 474H0Z" fill="var(--white)"/>
    <path d="M40 0C20 150 30 330 80 474H60C14 330 6 150 28 0Z" fill="var(--pink)"/>
  </svg>
  <div class="photo-inset" role="img" aria-label="Caregiver sharing a friendly moment with a senior woman"></div>

  <section class="left-column">
    <div class="brand">
      <span class="brand-mark"></span>
      <span class="brand-name">Brightmeadow<br>Homecare</span>
    </div>

    <h1 class="headline">Personal care services to meet your loved ones needs in the comfort and safety of their own home.</h1>

    <div class="services-tab">Homecare Services</div>
    <ul class="services">
      <li><svg viewBox="0 0 14 14"><rect width="14" height="14" rx="2" fill="var(--blue-pale)"/><path d="M3 7.5l2.5 2.5L11 4" fill="none" stroke="var(--blue-deep)" stroke-width="2"/></svg>Home Health Aides</li>
      <li><svg viewBox="0 0 14 14"><rect width="14" height="14" rx="2" fill="var(--blue-pale)"/><path d="M3 7.5l2.5 2.5L11 4" fill="none" stroke="var(--blue-deep)" stroke-width="2"/></svg>Skilled Nursing (RN/LPN)</li>
      <li><svg viewBox="0 0 14 14"><rect width="14" height="14" rx="2" fill="var(--blue-pale)"/><path d="M3 7.5l2.5 2.5L11 4" fill="none" stroke="var(--blue-deep)" stroke-width="2"/></svg>Bathing &amp; Meal Service</li>
      <li><svg viewBox="0 0 14 14"><rect width="14" height="14" rx="2" fill="var(--blue-pale)"/><path d="M3 7.5l2.5 2.5L11 4" fill="none" stroke="var(--blue-deep)" stroke-width="2"/></svg>Medication Management</li>
      <li><svg viewBox="0 0 14 14"><rect width="14" height="14" rx="2" fill="var(--blue-pale)"/><path d="M3 7.5l2.5 2.5L11 4" fill="none" stroke="var(--blue-deep)" stroke-width="2"/></svg>Services Available 24/7</li>
    </ul>

    <p class="consult">Call today for FREE Consultation</p>
    <svg class="heart-accent" viewBox="0 0 26 22" aria-hidden="true"><path d="M13 20C4 13 1 9 1 6a5 5 0 0 1 12-2 5 5 0 0 1 12 2c0 3-3 7-12 14z" fill="none" stroke="var(--blue)" stroke-width="2"/></svg>
  </section>

  <footer class="contact-bar">
    <div class="call-pill">
      <span class="call-label">Call Now</span>
      <svg viewBox="0 0 16 16"><path d="M4 1l3 3-2 2c1 2 3 4 5 5l2-2 3 3-2 3C7 15 1 9 1 3z" fill="var(--white)"/></svg>
      <span class="call-number">(808) 555-0173</span>
    </div>
    <div class="contact-item">
      <svg viewBox="0 0 16 16"><rect x="1" y="3" width="14" height="10" rx="1.5" fill="none" stroke="var(--white)" stroke-width="1.5"/><path d="M1.5 4l6.5 5 6.5-5" fill="none" stroke="var(--white)" stroke-width="1.5"/></svg>
      Info@brightmeadowcare.com
    </div>
    <div class="contact-item">
      <svg viewBox="0 0 16 16"><circle cx="8" cy="8" r="6.5" fill="none" stroke="var(--white)" stroke-width="1.5"/><path d="M1.5 8h13M8 1.5c3 3 3 10 0 13M8 1.5c-3 3-3 10 0 13" fill="none" stroke="var(--white)" stroke-width="1.2"/></svg>
      www.Brightmeadowcare.com
    </div>
  </footer>
</main>
</body>
</html>
```